Square Business Cards for Our Restaurant / Event Venue

We need square business cards designed for the management team of our event venue and restaurant. On one side of the card should be the the Harbor Lantern 7 logo and URL www.harborlantern7.example. On the other side should be the Ember Logo and URL www.emberhall7.example. All employee details should be on the side with Ember logo. There will be a total of 5 cards to be created with the design.

Clara Bennquist
clara@harborlantern7.example

main 555.418.3072
direct 555.730.2946

4831 West Orchard Lane SE
Washington, DC 90417

Industry/Entity Type

Business

```html
<!DOCTYPE html>
<html lang="en">
<head>
<meta charset="utf-8">
<title>Harbor Lantern 7 – Business Cards</title>
<link rel="stylesheet" href="https://fonts.googleapis.com/css2?family=Montserrat:wght@400;500;600;700&display=swap">
<style>
  :root {
    --backdrop: #9a9a9a;
    --card: #fbfbfb;
    --brand-red: #9c2822;
    --ink: #1c1c1c;
    --white: #ffffff;
  }
  html, body {
    margin: 0;
    padding: 0;
    overflow: hidden;
  }
  body {
    width: 1200px;
    height: 759px;
    background: var(--backdrop);
    position: relative;
    font-family: "Montserrat", Arial, sans-serif;
    color: var(--ink);
  }
  .card {
    position: absolute;
    top: 194px;
    width: 370px;
    height: 370px;
    background: var(--card);
    overflow: hidden;
  }
  .card--front { left: 188px; }
  .card--back { left: 641px; }

  /* Front */
  .brand-disc {
    position: absolute;
    left: 73px;
    top: 51px;
    width: 224px;
    height: 224px;
    border-radius: 50%;
    background: var(--brand-red);
    display: flex;
    align-items: center;
    justify-content: center;
    text-align: center;
  }
  .brand-name {
    color: var(--white);
    font-weight: 500;
    font-size: 25px;
    line-height: 1.2;
    letter-spacing: 0.5px;
  }
  .front-url {
    position: absolute;
    left: 0;
    right: 0;
    top: 328px;
    text-align: center;
    font-size: 15px;
    font-weight: 500;
  }
  .accent { color: var(--brand-red); }

  /* Back */
  .header-wave {
    position: absolute;
    left: 0;
    top: 0;
    width: 370px;
    height: 130px;
  }
  .person-name {
    position: absolute;
    right: 21px;
    top: 20px;
    margin: 0;
    color: var(--white);
    font-size: 25px;
    font-weight: 600;
    line-height: 26px;
    text-align: right;
  }
  .venue-name {
    position: absolute;
    left: 22px;
    top: 118px;
    margin: 0;
    font-size: 66px;
    font-weight: 700;
    color: var(--ink);
    letter-spacing: -1px;
  }
  .contact-list {
    position: absolute;
    left: 22px;
    top: 235px;
    margin: 0;
    padding: 0;
    list-style: none;
    font-size: 16px;
    font-weight: 500;
    line-height: 19.5px;
  }
  .contact-list li {
    display: flex;
    align-items: center;
    white-space: nowrap;
  }
  .icon {
    width: 13px;
    height: 13px;
    margin-right: 9px;
    flex: none;
  }
  .icon--inline { margin: 0 5px 0 6px; }
  .address {
    position: absolute;
    left: 22px;
    top: 301px;
    margin: 0;
    font-style: normal;
    font-size: 16px;
    font-weight: 500;
    line-height: 19.5px;
  }
</style>
</head>
<body>

<section class="card card--front">
  <div class="brand-disc">
    <span class="brand-name">Harbor<br>Lantern 7</span>
  </div>
  <p class="front-url" style="margin:0">www.<span class="accent">harborlantern7</span>.example</p>
</section>

<section class="card card--back">
  <svg class="header-wave" viewBox="0 0 370 130" aria-hidden="true">
    <path d="M0 0 H370 V106 C320 104 280 96 240 76 C180 46 120 6 0 12 Z" fill="var(--brand-red)"/>
    <path d="M0 28 C80 8 150 20 220 62 C270 92 320 110 370 108 V118 C310 122 265 104 215 74 C150 34 90 20 0 42 Z" fill="var(--ink)"/>
    <path d="M0 48 C70 28 130 34 200 66" fill="none" stroke="var(--ink)" stroke-width="2"/>
  </svg>

  <h2 class="person-name">Clara<br>Bennquist</h2>

  <h1 class="venue-name">Ember</h1>

  <ul class="contact-list">
    <li>
      <svg class="icon" viewBox="0 0 12 12" aria-hidden="true">
        <circle cx="6" cy="6" r="5.2" fill="none" stroke="var(--brand-red)" stroke-width="1.3"/>
        <path d="M1 6 H11 M6 1 C3 4 3 8 6 11 M6 1 C9 4 9 8 6 11" fill="none" stroke="var(--brand-red)" stroke-width="1"/>
      </svg>
      <span>www.<span class="accent">emberhall7</span>.example</span>
    </li>
    <li>
      <svg class="icon" viewBox="0 0 12 12" aria-hidden="true">
        <path d="M3 1 L5 3.5 L4 5 C5 7 6 8 7.5 8.5 L9 7.5 L11 9.5 L9.5 11 C5 11 1 7 1 2.5 Z" fill="none" stroke="var(--brand-red)" stroke-width="1.2"/>
      </svg>
      <span>555.418.3072</span>
      <svg class="icon icon--inline" viewBox="0 0 12 12" aria-hidden="true">
        <path d="M1 5 C1 2 11 2 11 5 L9 5.5 L8.5 4 H3.5 L3 5.5 Z" fill="var(--brand-red)"/>
        <rect x="2.5" y="6" width="7" height="4.5" rx="1" fill="var(--brand-red)"/>
      </svg>
      <span>555.730.2946</span>
    </li>
    <li>
      <svg class="icon" viewBox="0 0 12 12" aria-hidden="true">
        <rect x="0.5" y="2.5" width="11" height="7.5" fill="var(--brand-red)"/>
        <path d="M0.5 2.5 L6 7 L11.5 2.5" fill="none" stroke="var(--card)" stroke-width="1"/>
      </svg>
      <span>clara@<span class="accent">harborlantern7</span>.example</span>
    </li>
  </ul>

  <address class="address">
    4831 West Orchard Lane SE<br>
    Washington, DC 90417
  </address>
</section>

</body>
</html>
```